I need a Canva design for my company for real estate new listings

A new listing Canva template for properties we list, also a sold and under contract template. We are an outdoor brand thornbrookestates.com so it needs to flow with our designs.

```html
<!DOCTYPE html>
<html lang="en">
<head>
<meta charset="utf-8">
<title>Pitt County Swine Farm – New Listing</title>
<link rel="stylesheet" href="https://fonts.googleapis.com/css2?family=Playfair+Display:wght@400;500&family=Roboto:wght@400;500;700&display=swap">
<style>
  :root {
    --cream: #efece6;
    --espresso: #3d2b20;
    --copper: #8f5b37;
    --ink: #3a2b22;
    --white: #ffffff;
    --field: #6f8f52;
    --pond: #7c6a7a;
    --sky: #a9c4d6;
    --forest: #2f4a2c;
  }
  * { margin: 0; padding: 0; box-sizing: border-box; }
  html, body { width: 1200px; height: 1200px; overflow: hidden; }
  body { background: var(--cream); font-family: "Roboto", sans-serif; color: var(--ink); }
  .flyer { position: relative; width: 1200px; height: 1200px; background: var(--cream); }
  .brand-column { position: absolute; left: 694px; top: 0; width: 436px; height: 786px; background: var(--espresso); }
  .footer-band { position: absolute; left: 0; top: 889px; width: 1200px; height: 311px; background: var(--espresso); }

  .tag { position: absolute; left: 53px; top: 59px; height: 40px; padding: 0 14px; background: var(--espresso); color: var(--white); font-size: 25px; line-height: 40px; }
  .title { position: absolute; left: 72px; top: 108px; font-family: "Playfair Display", serif; font-weight: 400; font-size: 80px; line-height: 76px; color: var(--ink); }
  .price { position: absolute; left: 74px; top: 293px; font-size: 41px; font-weight: 700; color: var(--copper); }
  .price-rule { position: absolute; left: 74px; top: 357px; width: 240px; height: 3px; background: var(--copper); }
  .intro { position: absolute; left: 74px; top: 396px; width: 600px; font-size: 22px; line-height: 28px; }
  .highlights-title { position: absolute; left: 74px; top: 566px; font-size: 31px; font-weight: 700; color: var(--copper); }
  .highlights { position: absolute; top: 622px; list-style: none; font-size: 22px; line-height: 34px; }
  .highlights.col-a { left: 83px; }
  .highlights.col-b { left: 398px; width: 260px; }
  .highlights li { position: relative; padding-left: 31px; }
  .highlights li.wrap { line-height: 28px; padding-top: 3px; }
  .highlights li::before { content: ""; position: absolute; left: 0; top: 12px; width: 12px; height: 12px; border: 3px solid var(--copper); border-radius: 50%; }

  .brand { position: absolute; left: 694px; top: 95px; width: 436px; display: flex; align-items: center; justify-content: center; gap: 14px; color: var(--cream); font-family: "Roboto", sans-serif; font-size: 34px; font-weight: 500; }
  .brand-dot { width: 20px; height: 20px; border-radius: 50%; background: var(--cream); }

  .photo { position: absolute; border: 4px solid var(--white); }
  .photo-farm { left: 966px; }
  .photo-1 { left: 732px; top: 286px; width: 360px; height: 211px; background: linear-gradient(120deg, var(--sky) 0%, #7fa071 35%, var(--pond) 70%, var(--field) 100%); }
  .photo-2 { left: 732px; top: 529px; width: 360px; height: 210px; background: linear-gradient(180deg, var(--forest) 0%, var(--pond) 30%, #7a9a5a 60%, var(--field) 100%); }
  .photo-main { position: absolute; left: 53px; top: 786px; width: 1093px; height: 300px; background: linear-gradient(180deg, #b9cfdd 0%, #b9cfdd 8%, var(--forest) 12%, #3c5a35 40%, #6f8f5a 60%, #7a6c78 80%, #6c8d4f 100%); }

  .ribbon { position: absolute; left: 924px; top: 770px; width: 236px; height: 240px; }
  .contact { position: absolute; left: 53px; top: 1087px; width: 1093px; height: 64px; border: 3px solid var(--white); display: flex; font-size: 26px; font-weight: 700; }
  .contact > div { display: flex; align-items: center; justify-content: center; }
  .contact-label { width: 374px; background: var(--copper); color: var(--white); }
  .contact-phone { width: 289px; background: var(--white); color: var(--ink); gap: 10px; }
  .contact-web { flex: 1; background: var(--espresso); color: var(--white); }
</style>
</head>
<body>
<main class="flyer">
  <div class="brand-column"></div>
  <div class="footer-band"></div>

  <div class="tag">New Listing</div>
  <h1 class="title">Pitt County<br>Swine Farm</h1>
  <div class="price">$4,000,000</div>
  <div class="price-rule"></div>
  <p class="intro">Exceptional opportunity to own a modern, income-producing swine operation in Pitt County. This 126± acre property features four well-maintained swine houses built in 2019 and is currently operating as a wean-to-finish facility with a total capacity of 14,144 head space.</p>

  <h2 class="highlights-title">Property Highlights:</h2>
  <ul class="highlights col-a">
    <li>126± acres</li>
    <li>4 modern swine houses</li>
    <li>Wean-to-finish operation</li>
    <li>14,144 head capacity</li>
  </ul>
  <ul class="highlights col-b">
    <li>Houses built in 2019</li>
    <li>1 center pivot</li>
    <li class="wrap">Contract in place through 2034</li>
  </ul>

  <div class="brand"><span class="brand-dot"></span>Thornbrook Estates</div>

  <div class="photo photo-1" role="img" aria-label="Aerial view of swine houses beside a lagoon and green fields"></div>
  <div class="photo photo-2" role="img" aria-label="Aerial view of a lagoon, open field and small farm buildings"></div>
  <div class="photo-main" role="img" aria-label="Aerial view of four swine houses with feed bins, ponds and surrounding forest"></div>

  <svg class="ribbon" viewBox="0 0 236 240" aria-hidden="true">
    <polygon points="0,4 222,4 232,14 232,236 220,224" fill="#8f5b37"/>
    <polygon points="0,4 10,0 222,0 222,4" fill="#6e4428"/>
    <g transform="translate(150,86) rotate(45)" fill="#ffffff" font-family="Roboto, sans-serif" text-anchor="middle">
      <text x="0" y="-6" font-size="26" font-weight="400">PRICE</text>
      <text x="0" y="26" font-size="30" font-weight="700">$4,000,000</text>
    </g>
  </svg>

  <div class="contact">
    <div class="contact-label">Get in touch:</div>
    <div class="contact-phone">
      <svg width="18" height="20" viewBox="0 0 24 24" aria-hidden="true"><path fill="#8f5b37" d="M6.6 10.8a15.1 15.1 0 0 0 6.6 6.6l2.2-2.2a1 1 0 0 1 1-.25 11.4 11.4 0 0 0 3.6.57 1 1 0 0 1 1 1V20a1 1 0 0 1-1 1A17 17 0 0 1 3 4a1 1 0 0 1 1-1h3.5a1 1 0 0 1 1 1c0 1.25.2 2.45.57 3.57a1 1 0 0 1-.25 1z"/></svg>
      (555) 014-2876
    </div>
    <div class="contact-web">www.thornbrookestates.com</div>
  </div>
</main>
</body>
</html>
```